Electrician Company Website Design

I am looking to get a website designed only. I do not need it converted ot html. I simply need the design in a psd format. I have my own team for the conversion. The website is for an electrician company called Bramblecourt electric. I have created a txt document with the project parameters and specifics. I have also uploaded their logo in all avaible formats. It's a zip file.

Number of Pages Required

1 page

```html
<!DOCTYPE html>
<html lang="en">
<head>
<meta charset="utf-8">
<title>Bramblecourt Electric</title>
<link href="https://fonts.googleapis.com/css2?family=Roboto:wght@400;500;700&family=Raleway:wght@400;500&display=swap" rel="stylesheet">
<style>
:root{
  --blue:#1f5fb5;
  --blue-dark:#184d96;
  --red:#a32424;
  --red-band:#9a2528;
  --navy:#0d1b33;
  --ink:#1a1a1a;
  --body:#555;
  --field:#f3f3f3;
  --white:#fff;
}
*{box-sizing:border-box;margin:0;padding:0}
html,body{width:1200px;height:4882px;overflow:hidden}
body{position:relative;background:var(--white);font-family:'Raleway',sans-serif;color:var(--ink)}
.abs{position:absolute}
.btn{position:absolute;display:flex;align-items:center;justify-content:center;font:500 14px 'Roboto',sans-serif;color:var(--white);height:36px;width:156px}
.btn--red{background:var(--red)}
.btn--blue{background:var(--blue)}
.btn--outline{border:1.5px solid var(--red);color:var(--red);background:var(--white)}
.h2{position:absolute;font:700 34px 'Roboto',sans-serif;letter-spacing:.3px}
.rule{position:absolute;height:3px;width:100px;background:var(--blue)}
.para{position:absolute;font-size:14px;line-height:24px;color:var(--body)}
.photo{position:absolute}

/* header */
.topbar{left:862px;top:0;width:238px;height:24px;background:var(--blue);color:var(--white);font:500 11px 'Roboto',sans-serif;display:flex;align-items:center;justify-content:center;gap:8px}
.brand{left:108px;top:20px;display:flex;align-items:center;gap:10px;font:700 17px 'Roboto',sans-serif;color:var(--navy)}
.brand__dot{width:36px;height:36px;border-radius:50%;background:var(--navy)}
.nav{left:548px;top:40px;display:flex;gap:26px;font:500 11px 'Roboto',sans-serif;color:var(--ink)}
.nav .is-active{color:var(--red)}

/* hero */
.hero{left:0;top:80px;width:1200px;height:612px}
.hero__kicker{left:553px;top:208px;font:400 19px 'Raleway',sans-serif;letter-spacing:4px;color:var(--white)}
.hero__title{left:553px;top:238px;font:700 60px/72px 'Roboto',sans-serif;color:var(--white)}

/* about */
.about__img{left:74px;top:795px;width:420px;height:420px;border-radius:50%;background:radial-gradient(circle,#c9d1dc 0%,#9aa7b8 60%,#7a8aa1 100%)}
.about__arc{left:74px;top:795px}

/* services */
.services{left:0;top:1323px;width:1200px;height:640px;background:linear-gradient(180deg,#2a66b8,#1d58a8)}
.card{position:absolute;top:1485px;width:321px;height:413px;background:var(--white)}
.card__img{height:186px}
.card__title{position:absolute;top:210px;width:100%;text-align:center;font:700 13px 'Roboto',sans-serif}
.card__text{position:absolute;top:240px;left:22px;right:22px;text-align:center;font-size:10px;line-height:18px;color:var(--body)}
.card .btn{top:345px;left:82px}

/* areas */
.area{position:absolute;display:flex;align-items:center;gap:14px;font:500 13px 'Roboto',sans-serif}
.pin{width:18px;height:18px;border:1px solid var(--red);border-radius:50%;display:flex;align-items:center;justify-content:center}

/* gallery */
.gallery{left:0;top:2480px;width:1200px;height:624px;background:linear-gradient(180deg,#a32a2d,#962226)}

/* faq */
.faq{position:absolute;height:54px;background:#f6f6f6;display:flex;align-items:center;justify-content:space-between;padding:0 13px;font:500 13px 'Roboto',sans-serif}
.faq .plus{font:300 22px 'Roboto',sans-serif;color:#666}

/* form */
.label{position:absolute;font:500 14px 'Roboto',sans-serif;letter-spacing:1px}
.field{position:absolute;background:var(--field);font-size:10px;color:#999;padding:14px 12px}

/* footer */
.footer{left:0;top:4440px;width:1200px;height:442px}
.ft-h{position:absolute;font:500 22px 'Roboto',sans-serif;color:var(--white)}
.ft-link{position:absolute;left:100px;font-size:13px;color:#dbe6f7}
.ft-row{position:absolute;left:336px;display:flex;align-items:center;gap:18px;font-size:13px;color:#dbe6f7}
.ft-ico{width:28px;height:28px;border-radius:50%;background:var(--white);display:flex;align-items:center;justify-content:center}
.social{position:absolute;top:4770px;width:26px;height:26px;border-radius:50%;background:var(--white);display:flex;align-items:center;justify-content:center}
.social span{width:12px;height:12px;background:var(--red);border-radius:2px}
.copyright{left:0;top:4844px;width:1200px;height:38px;background:#174a92;color:var(--white);font:400 13px 'Roboto',sans-serif;display:flex;align-items:center;justify-content:center}
</style>
</head>
<body>

<!-- header -->
<div class="abs topbar">
  <svg width="12" height="12" viewBox="0 0 24 24" fill="none" stroke="#fff" stroke-width="2"><path d="M22 16.9v3a2 2 0 0 1-2.2 2 19.8 19.8 0 0 1-8.6-3.1 19.5 19.5 0 0 1-6-6A19.8 19.8 0 0 1 2.1 4.2 2 2 0 0 1 4.1 2h3a2 2 0 0 1 2 1.7c.1.9.4 1.8.7 2.7a2 2 0 0 1-.5 2.1L8 9.8a16 16 0 0 0 6 6l1.3-1.3a2 2 0 0 1 2.1-.4c.9.3 1.8.6 2.7.7a2 2 0 0 1 1.7 2z"/></svg>
  Contact Us On 555 204 7731
</div>
<div class="abs brand"><span class="brand__dot"></span>Bramblecourt Electric</div>
<nav class="abs nav">
  <span class="is-active">Home</span><span>About Company</span><span>Our Services</span><span>Service Areas</span><span>Our Gallery</span><span>FAQ's</span><span>Contact Us</span>
</nav>

<!-- hero -->
<svg class="abs hero" viewBox="0 0 1200 612" role="img" aria-label="Dark interior with glowing pendant lamps hanging by a window">
  <defs>
    <linearGradient id="heroBg" x1="0" y1="0" x2="1" y2="0">
      <stop offset="0" stop-color="#3b3a3a"/><stop offset=".45" stop-color="#1d2a40"/><stop offset="1" stop-color="#13213a"/>
    </linearGradient>
  </defs>
  <path d="M0 0H1200V500Q1120 540 860 545Q700 555 600 612Q500 555 340 545Q80 540 0 500Z" fill="url(#heroBg)"/>
  <path d="M0 490Q40 560 340 575Q520 585 600 615Q680 585 860 575Q1160 560 1200 490V520Q1140 590 860 595Q690 605 600 612Q510 605 340 595Q60 590 0 520Z" fill="var(--blue)"/>
  <path d="M0 500Q30 570 340 585Q510 592 600 612Q490 560 340 545Q80 540 0 500Z" fill="var(--blue)"/>
  <path d="M1200 500Q1170 570 860 585Q690 592 600 612Q710 560 860 545Q1120 540 1200 500Z" fill="var(--blue)"/>
</svg>
<div class="abs hero__kicker">WE ARE BRAMBLECOURT ELECTRIC</div>
<div class="abs hero__title">FAST ELECTRICAL<br>SERVICE PROVIDER</div>
<div class="btn btn--red" style="left:553px;top:428px">Contact Us</div>
<div class="btn btn--blue" style="left:727px;top:428px">Our Services</div>

<!-- about -->
<div class="photo about__img" role="img" aria-label="Smiling electrician in a blue uniform and yellow hard hat holding a wrench and tool case"></div>
<svg class="abs about__arc" width="420" height="440" viewBox="0 0 420 440"><path d="M0 210A210 210 0 0 0 420 210" fill="none" stroke="var(--blue)" stroke-width="12"/></svg>
<div class="h2" style="left:607px;top:818px">ABOUT US</div>
<p class="para" style="left:607px;top:898px;width:500px">Lorem ipsum dolor sit amet consectetur. Ultricies id curabitur commodo amet enim elementum gravida. Commodo semper vestibulum in nisl sed. At dolor ac neque ipsum purus auctor sem sem. Netus velit posuere sit varius gravida consequat euismod arcu purus. Tincidunt vivamus odio egestas nulla elementum non a nibh. Vitae volutpat nulla scelerisque adipiscing amet at egestas. Elementum quisque amet scelerisque id non pharetra integer purus quam. Viverra quis amet sed et scelerisque egestas semper lectus. Amet aliquam et volutpat dignissim morbi turpis elementum est sed.</p>
<div class="btn btn--red" style="left:607px;top:1162px">Read More</div>

<!-- services -->
<div class="abs services" role="img" aria-label="Blue-tinted electrical equipment backdrop"></div>
<div class="h2" style="left:0;width:1200px;text-align:center;top:1385px;color:var(--white)">OUR SERVICES</div>
<div class="rule" style="left:550px;top:1432px;background:var(--white)"></div>

<div class="card" style="left:100px">
  <div class="card__img" style="background:linear-gradient(135deg,#6f7f96,#b8c0c8)" role="img" aria-label="Lineman working on a steel power pylon"></div>
  <div class="card__title">COMMERICAL ELECTRICAL SERVICES</div>
  <div class="card__text">Lorem ipsum dolor sit amet consectetur. Ultricies id curabitur commodo amet enim elementum gravida. Commodo semper vestibulum in nisl sed. At dolor ac neque ipsum purus auctor sem sem. Netus velit</div>
  <div class="btn btn--outline">Read More</div>
</div>
<div class="card" style="left:440px">
  <div class="card__img" style="background:linear-gradient(180deg,#1f2a26,#3b3a30)" role="img" aria-label="Modern house lit at dusk among trees"></div>
  <div class="card__title">RESIDENTIAL ELECTRICAL SERVICES</div>
  <div class="card__text">Lorem ipsum dolor sit amet consectetur. Ultricies id curabitur commodo amet enim elementum gravida. Commodo semper vestibulum in nisl sed. At dolor ac neque ipsum purus auctor sem sem. Netus velit</div>
  <div class="btn btn--outline">Read More</div>
</div>
<div class="card" style="left:779px">
  <div class="card__img" style="background:linear-gradient(135deg,#8a7a66,#c6c0b4)" role="img" aria-label="Electrician in a hard hat working on a fuse board"></div>
  <div class="card__title">INDUSTRIAL ELECTRICAL SERVICES</div>
  <div class="card__text">Lorem ipsum dolor sit amet consectetur. Ultricies id curabitur commodo amet enim elementum gravida. Commodo semper vestibulum in nisl sed. At dolor ac neque ipsum purus auctor sem sem. Netus velit</div>
  <div class="btn btn--outline">Read More</div>
</div>

<!-- service areas -->
<div class="h2" style="left:100px;top:2056px">SERVICE AREAS</div>
<p class="para" style="left:100px;top:2132px;width:505px">Lorem ipsum dolor sit amet consectetur. Ultricies id curabitur commodo amet enim elementum gravida. Commodo semper vestibulum in nisl sed. At dolor ac neque ipsum purus auctor sem sem. Netus velit posuere</p>
<div class="area" style="left:100px;top:2237px"><span class="pin"><svg width="8" height="10" viewBox="0 0 8 10"><path d="M4 10C1 6 0 5 0 4a4 4 0 0 1 8 0c0 1-1 2-4 6z" fill="var(--red)"/></svg></span>ALDERTON MN</div>
<div class="area" style="left:277px;top:2237px"><span class="pin"><svg width="8" height="10" viewBox="0 0 8 10"><path d="M4 10C1 6 0 5 0 4a4 4 0 0 1 8 0c0 1-1 2-4 6z" fill="var(--red)"/></svg></span>ALDERTON MN</div>
<div class="area" style="left:449px;top:2237px"><span class="pin"><svg width="8" height="10" viewBox="0 0 8 10"><path d="M4 10C1 6 0 5 0 4a4 4 0 0 1 8 0c0 1-1 2-4 6z" fill="var(--red)"/></svg></span>ALDERTON MN</div>
<div class="area" style="left:100px;top:2275px"><span class="pin"><svg width="8" height="10" viewBox="0 0 8 10"><path d="M4 10C1 6 0 5 0 4a4 4 0 0 1 8 0c0 1-1 2-4 6z" fill="var(--red)"/></svg></span>ALDERTON MN</div>
<div class="area" style="left:277px;top:2275px"><span class="pin"><svg width="8" height="10" viewBox="0 0 8 10"><path d="M4 10C1 6 0 5 0 4a4 4 0 0 1 8 0c0 1-1 2-4 6z" fill="var(--red)"/></svg></span>ALDERTON MN</div>
<div class="area" style="left:449px;top:2275px"><span class="pin"><svg width="8" height="10" viewBox="0 0 8 10"><path d="M4 10C1 6 0 5 0 4a4 4 0 0 1 8 0c0 1-1 2-4 6z" fill="var(--red)"/></svg></span>ALDERTON MN</div>
<div class="btn btn--blue" style="left:100px;top:2345px">Read More</div>
<div class="abs" style="left:864px;top:2070px;width:236px;height:317px;background:var(--blue)"></div>
<div class="photo" style="left:711px;top:2057px;width:375px;height:317px;background:linear-gradient(135deg,#2e3238,#8b9097 60%,#c9ccd0)" role="img" aria-label="Electrician in a white hard hat wiring a distribution panel"></div>

<!-- gallery -->
<div class="abs gallery" role="img" aria-label="Red-tinted electrical workshop backdrop"></div>
<div class="h2" style="left:0;width:1200px;text-align:center;top:2543px;color:var(--white)">OUR GALLERY</div>
<div class="rule" style="left:550px;top:2590px;background:var(--white)"></div>
<div class="photo" style="left:100px;top:2639px;width:306px;height:404px;background:linear-gradient(180deg,#5a4a40,#7c8a6a)" role="img" aria-label="Electrician checking an outdoor meter box"></div>
<div class="photo" style="left:417px;top:2639px;width:319px;height:199px;background:linear-gradient(180deg,#6b9bd0,#2d4f86)" role="img" aria-label="Technician installing rooftop solar panels"></div>
<div class="photo" style="left:747px;top:2639px;width:353px;height:199px;background:linear-gradient(135deg,#2e3238,#9aa0a6)" role="img" aria-label="Electrician working inside a breaker panel"></div>
<div class="photo" style="left:417px;top:2844px;width:199px;height:199px;background:linear-gradient(135deg,#1f2f5c,#5a7fb0)" role="img" aria-label="Hands holding coloured cable wires"></div>
<div class="photo" style="left:626px;top:2844px;width:265px;height:199px;background:linear-gradient(135deg,#2a2c30,#7d8288)" role="img" aria-label="Electrician connecting wires in a switchboard"></div>
<div class="photo" style="left:901px;top:2844px;width:199px;height:199px;background:linear-gradient(135deg,#a8aeb5,#e3e5e8)" role="img" aria-label="Electrician in a white helmet at a fuse panel"></div>

<!-- faq -->
<div class="h2" style="left:0;width:1200px;text-align:center;top:3196px">FREQUENTLY ASKED QUESTION</div>
<div class="rule" style="left:550px;top:3242px"></div>
<div class="abs" style="left:100px;top:3309px;width:494px;height:84px;background:var(--red);color:var(--white);font:500 13px/30px 'Roboto',sans-serif;padding:12px 13px">
  Lorem ipsum dolor sit amet, consectetur adipiscing elit.<br>Non nibh ultrices volutpat ullamcorper ?
  <span style="position:absolute;right:16px;top:12px;font-size:20px">–</span>
</div>
<div class="abs" style="left:100px;top:3393px;width:494px;height:95px;background:#f6f6f6;font-size:10px;line-height:18px;color:var(--body);padding:12px 13px">Lorem ipsum dolor sit amet, consectetur adipiscing elit. Tempor scelerisque tempor sollicitudin imperdiet. At integer sed quam nunc, risus pretium, ligula quis tellus. Tempor tincidunt porttitor nunc nascetur elementum mauris tortor eu, sit. Vulputate mauris porttitor eget eget volutpat, mauris morbi.</div>
<div class="faq" style="left:100px;top:3512px;width:494px">Lorem ipsum dolor sit amet, consectetur adipiscing elit.<span class="plus">+</span></div>
<div class="faq" style="left:100px;top:3580px;width:494px">Lorem ipsum dolor sit amet, consectetur adipiscing elit.<span class="plus">+</span></div>
<div class="faq" style="left:609px;top:3309px;width:491px">Lorem ipsum dolor sit amet, consectetur adipiscing elit.<span class="plus">+</span></div>
<div class="faq" style="left:609px;top:3377px;width:491px">Lorem ipsum dolor sit amet, consectetur adipiscing elit.<span class="plus">+</span></div>
<div class="faq" style="left:609px;top:3445px;width:491px">Lorem ipsum dolor sit amet, consectetur adipiscing elit.<span class="plus">+</span></div>
<div class="faq" style="left:609px;top:3512px;width:491px">Lorem ipsum dolor sit amet, consectetur adipiscing elit.<span class="plus">+</span></div>
<div class="faq" style="left:609px;top:3580px;width:491px">Lorem ipsum dolor sit amet, consectetur adipiscing elit.<span class="plus">+</span></div>
<div class="btn btn--blue" style="left:523px;top:3684px">Read All</div>

<!-- contact form -->
<div class="h2" style="left:100px;top:3816px">GET IN TOUCH</div>
<div class="label" style="left:100px;top:3895px">First Name:</div>
<div class="label" style="left:381px;top:3895px">Last Name:</div>
<div class="field" style="left:100px;top:3923px;width:251px;height:38px;background:var(--white);border:1px solid #999;color:#333;padding:10px 10px">|</div>
<div class="field" style="left:381px;top:3923px;width:251px;height:38px">Write Here</div>
<div class="label" style="left:100px;top:3982px">Phone Number:</div>
<div class="label" style="left:381px;top:3982px">Email:</div>
<div class="field" style="left:100px;top:4010px;width:251px;height:37px">Write Here</div>
<div class="field" style="left:381px;top:4010px;width:251px;height:37px">Write Here</div>
<div class="label" style="left:100px;top:4068px">Message:</div>
<div class="field" style="left:100px;top:4096px;width:532px;height:75px">Write Here</div>
<div class="btn btn--red" style="left:100px;top:4222px">Send</div>
<div class="abs" style="left:864px;top:3940px;width:236px;height:317px;background:var(--blue)"></div>
<div class="photo" style="left:713px;top:3815px;width:373px;height:426px;background:linear-gradient(160deg,#c9cfd6,#e8ebee 50%,#a9b0b8)" role="img" aria-label="Electrician in a yellow hard hat fitting wiring to a solar panel"></div>

<!-- footer -->
<svg class="abs footer" viewBox="0 0 1200 442">
  <path d="M0 90Q60 30 300 30Q520 25 600 0Q680 25 900 30Q1140 30 1200 90V442H0Z" fill="var(--red)"/>
  <path d="M0 100Q60 50 300 50Q520 45 600 22Q680 45 900 50Q1140 50 1200 100V442H0Z" fill="var(--blue)"/>
</svg>
<div class="abs" style="left:535px;top:4335px;width:130px;height:130px;border-radius:50%;background:var(--navy);display:flex;align-items:center;justify-content:center;text-align:center;font:700 15px/19px 'Roboto',sans-serif;color:var(--white)">Bramblecourt<br>Electric</div>

<div class="ft-h" style="left:100px;top:4547px">Quick Links</div>
<div class="ft-link" style="top:4595px">Home</div>
<div class="ft-link" style="top:4625px">About Us</div>
<div class="ft-link" style="top:4655px">Our Services</div>
<div class="ft-link" style="top:4685px">Service Areas</div>
<div class="ft-link" style="top:4715px">Our Gallery</div>
<div class="ft-link" style="top:4745px">FAQ's</div>
<div class="ft-link" style="top:4775px">Contact Us</div>

<div class="ft-h" style="left:336px;top:4547px">Contact Info</div>
<div class="ft-row" style="top:4592px"><span class="ft-ico"><svg width="12" height="12" viewBox="0 0 24 24"><path d="M22 16.9v3a2 2 0 0 1-2.2 2 19.8 19.8 0 0 1-8.6-3.1 19.5 19.5 0 0 1-6-6A19.8 19.8 0 0 1 2.1 4.2 2 2 0 0 1 4.1 2h3a2 2 0 0 1 2 1.7l.7 2.7a2 2 0 0 1-.5 2.1L8 9.8a16 16 0 0 0 6 6l1.3-1.3a2 2 0 0 1 2.1-.4l2.7.7a2 2 0 0 1 1.7 2z" fill="var(--red)"/></svg></span>555 204 7731</div>
<div class="ft-row" style="top:4636px"><span class="ft-ico"><svg width="10" height="12" viewBox="0 0 8 10"><path d="M4 10C1 6 0 5 0 4a4 4 0 0 1 8 0c0 1-1 2-4 6z" fill="var(--red)"/></svg></span>14 Alderton Road, Suite 3</div>
<div class="ft-row" style="top:4680px"><span class="ft-ico"><svg width="12" height="10" viewBox="0 0 12 10"><rect x=".5" y=".5" width="11" height="9" fill="none" stroke="var(--red)"/><path d="M.5 .5L6 5l5.5-4.5" fill="none" stroke="var(--red)"/></svg></span>office@bramblecourtmail.com</div>

<div class="ft-h" style="left:686px;top:4547px">Newsletter</div>
<p class="abs" style="left:686px;top:4597px;width:360px;font-size:13px;line-height:24px;color:#dbe6f7">Contact us using this form. A representative will answer your question as soon as possible</p>
<div class="abs" style="left:686px;top:4674px;width:334px;height:62px;background:var(--white);font-size:10px;padding:24px 24px;color:#333">Email</div>
<div class="abs" style="left:1020px;top:4674px;width:80px;height:62px;background:var(--red);display:flex;align-items:center;justify-content:center">
  <svg width="22" height="22" viewBox="0 0 24 24" fill="none" stroke="#fff" stroke-width="1.8"><path d="M22 2L11 13M22 2l-7 20-4-9-9-4z"/></svg>
</div>
<div class="social" style="left:689px"><span></span></div>
<div class="social" style="left:740px"><span></span></div>
<div class="social" style="left:789px"><span></span></div>

<div class="abs copyright">Bramblecourt Electric ©2022</div>
</body>
</html>
```